Finiding oppertunites in Real Estate 6.15.20

size of ad 7” x 9.6”
1-I like the ad to stand out and attract people's attention.
2-you should be able to see the text of the ad clearly .. see the attachment anything in yellow is instructions.
3-the list of topics should not be the main part of the ad
4-if you decide you want a picture or vector of a person .. (you decide)
then it should be a white male about 25-30 years old wearing a solid white or blue shirt and not long hair.
5-leave 1 inch for footer
see attachment
Good luck

Target Market(s)

potential male students 25-35 years of age

Industry/Entity Type

Education

Requirements
Must have
• will stand out and people would want to see it.
should be able to read the words of ad
Nice to have
• how to make money in real estate on one line

```html
<!DOCTYPE html>
<html lang="en">
<head>
<meta charset="utf-8">
<title>Real Estate Career Course</title>
<link href="https://fonts.googleapis.com/css2?family=Lexend:wght@300;400;600;700;800&display=swap" rel="stylesheet">
<style>
  :root {
    --page-bg: #ffffff;
    --ink-dark: #333335;
    --panel-dark: #2b2f3b;
    --brand-blue: #2f5bb2;
    --panel-blue: #2f56a6;
    --white: #ffffff;
    --photo-grey-a: #d9dcdf;
    --photo-grey-b: #8f959c;
    --sky-a: #eef2f6;
    --sky-b: #8796a8;
  }
  * { margin: 0; padding: 0; box-sizing: border-box; }
  html, body {
    width: 1200px; height: 924px; overflow: hidden;
    background: var(--page-bg);
    font-family: "Lexend", "Montserrat", sans-serif;
  }
  .flyer {
    position: absolute; left: 280px; top: 23px;
    width: 640px; height: 878px;
    background: var(--white);
    box-shadow: 0 1px 4px rgba(0,0,0,0.25);
    overflow: hidden;
  }
  .masthead {
    position: absolute; left: 0; top: 0; width: 640px; height: 88px;
    background: var(--ink-dark);
    color: var(--white);
    display: flex; align-items: center; justify-content: center;
    font-weight: 700; font-size: 33px; letter-spacing: 0.2px;
  }
  .hero-backdrop {
    position: absolute; left: 0; top: 88px; width: 640px; height: 343px;
    background: linear-gradient(90deg, var(--photo-grey-b) 0%, var(--photo-grey-a) 40%, #e8eaec 100%);
  }
  .hero-portrait {
    position: absolute; left: 313px; top: 88px; width: 327px; height: 343px;
    background: linear-gradient(160deg, #f1f2f3 0%, #d6d9dc 55%, #a9aeb4 100%);
  }
  .hero-panel {
    position: absolute; left: 38px; top: 88px; width: 275px; height: 343px;
    background: var(--panel-blue);
    color: var(--white);
    text-align: center;
  }
  .hero-question {
    position: absolute; top: 30px; left: 0; width: 100%;
    line-height: 0.95; text-transform: uppercase;
  }
  .hero-question .q-light { font-weight: 300; font-size: 29px; display: block; }
  .hero-question .q-money { font-weight: 700; font-size: 37px; }
  .hero-question .q-in { font-weight: 300; font-size: 29px; }
  .hero-question .q-big { font-weight: 300; font-size: 48px; display: block; }
  .hero-audience {
    position: absolute; top: 217px; left: 0; width: 100%;
    font-weight: 300; font-size: 18px; line-height: 23px;
    text-transform: uppercase;
  }
  .building-photo {
    position: absolute; left: 38px; top: 431px; width: 275px; height: 126px;
    background: linear-gradient(180deg, var(--sky-a) 0%, #c4ccd6 50%, var(--sky-b) 100%);
  }
  .knowledge-panel {
    position: absolute; left: 313px; top: 431px; width: 327px; height: 126px;
    background: var(--panel-dark);
    color: var(--white);
    padding: 16px 0 0 33px;
    font-size: 21px; line-height: 25.5px; font-weight: 300;
    text-transform: uppercase;
  }
  .knowledge-panel b { font-weight: 600; }
  .remote-badge {
    position: absolute; left: 55px; top: 557px; width: 240px; height: 113px;
  }
  .remote-badge svg { position: absolute; left: 0; top: 0; }
  .remote-badge .badge-text {
    position: absolute; left: 0; top: 30px; width: 100%;
    text-align: center; color: var(--white);
    font-weight: 800; font-size: 27px; line-height: 24px;
    transform: rotate(-6deg);
  }
  .schedule {
    position: absolute; left: 346px; top: 573px;
    color: var(--panel-dark); text-transform: uppercase;
  }
  .schedule .sessions { font-weight: 700; font-size: 19px; line-height: 20px; }
  .schedule .starting { font-weight: 300; font-size: 19px; line-height: 20px; }
  .schedule .date {
    font-weight: 700; font-size: 50px; line-height: 46px;
    color: var(--brand-blue);
  }
  .topics-heading {
    position: absolute; left: 0; top: 670px; width: 640px; height: 29px;
    background: var(--ink-dark); color: var(--white);
    text-align: center; font-weight: 600; font-size: 19px; line-height: 29px;
  }
  .topics-list {
    position: absolute; left: 0; top: 699px; width: 640px; height: 87px;
    background: var(--brand-blue); color: var(--white);
  }
  .topics-list ul {
    position: absolute; top: 8px; list-style: none;
    font-weight: 300; font-size: 11.5px; line-height: 14.7px;
  }
  .topics-list li::before { content: "\2022\00a0"; font-weight: 700; }
  .col-one { left: 54px; }
  .col-two { left: 247px; }
  .col-three { left: 445px; }
</style>
</head>
<body>
  <main class="flyer">
    <header class="masthead">REAL ESTATE CAREER COURSE</header>

    <div class="hero-backdrop" role="img" aria-label="Blurred city street background"></div>
    <div class="hero-portrait" role="img" aria-label="Photo of a young man in a white shirt holding a tablet"></div>

    <section class="hero-panel">
      <h1 class="hero-question">
        <span class="q-light">How to make</span>
        <span class="q-money">MONEY</span> <span class="q-in">IN</span>
        <span class="q-big">REAL</span>
        <span class="q-big">ESTATE?</span>
      </h1>
      <p class="hero-audience">For those who<br>have started<br>or would like to go<br>into real estate</p>
    </section>

    <div class="building-photo" role="img" aria-label="Photo of a glass office tower against the sky"></div>

    <section class="knowledge-panel">
      An <b>investment</b> in<br><b>knowledge</b> opens<br>up untold<br><b>opportunities</b>
    </section>

    <div class="remote-badge">
      <svg width="240" height="113" viewBox="0 0 240 113" aria-hidden="true">
        <polygon fill="#111" points="120,2 138,18 165,6 170,28 205,24 192,44 232,52 198,66 220,88 182,86 176,113 150,96 120,113 96,96 66,113 60,88 22,92 40,68 6,54 44,44 32,22 70,26 80,4 102,18"/>
      </svg>
      <div class="badge-text">REMOTE<br>SESSIONS</div>
    </div>

    <section class="schedule">
      <div class="sessions">12 Session Course</div>
      <div class="starting">Classes starting</div>
      <div class="date">JUNE 16</div>
    </section>

    <h2 class="topics-heading">A PARTIAL LISTING OF TOPICS</h2>
    <section class="topics-list">
      <ul class="col-one">
        <li>SINGLE-FAMILY</li>
        <li>MULTIFAMILY</li>
        <li>MANAGEMENT</li>
        <li>REAL ESTATE CONCEPTS</li>
        <li>REAL ESTATE LAW</li>
      </ul>
      <ul class="col-two">
        <li>INVESTMENT PROPERTIES</li>
        <li>FORECLOSURES</li>
        <li>REHAB</li>
        <li>FORECLOSURES</li>
        <li>SHORT SALES</li>
      </ul>
      <ul class="col-three">
        <li>DEVELOPMENT</li>
        <li>FINANCIAL MODELING</li>
        <li>HUD PROPERTIES</li>
        <li>DUE DILIGENCE</li>
      </ul>
    </section>
  </main>
</body>
</html>
```